Steady Yield Contract Playbooks for busy people

"Necessity is the mother of invention"

The idea of vetting investment strategies is not new in the financial world before investing real monies. Vetting strategies in options strategies always have been a difficult exercise. Such exercise requires access to programmers, right tools and good historical data. These factors make vetting process very costly and tedious. Becuase of this reason, this process is mostly limited to hedge funds, private banking, wealth management firms. Very few products existed in the market to support this process.

Since my graduation in engineering with major in Computer Science, I worked in large global banks as an IT consultant. Over there, I was designing, developing or managing large IT projects. This job profile demanded long hours, busy and tiring days. Very few hours or literally, not enough time available to analyze investment opportunities.

Moreover, investing in stocks without understanding valuation, business model and financials of the companies often result in losses. More so, if not enough understanding on when to exit from a position. Entering into a position is easy and it is in trader's control but exiting a position when profiting and cutting losses is an important step to make money consistently. This needed more disciplined approach and defined rules for position sizing, money management, profit taking and cutting losses.

Options have greeks that will affect its pricing. Understanding and leading options is another major step in the hurdle of investing in options. There are good mentors/experts teaching options. Gaining conceptual understanding is not that difficult. Practically seeing the market affecting the options trades is the most difficult step. Mentors/experts use primitive tools that give some peek into the practical process but it is very tedious since they often provide manual backtesting. "Options" provide options. There are a lot of questions that need to be answered.

Which options strategy is right?
How to select the expiration date for each options strategy?
How to select the strikes involved in options strategy?
There is an option to paper trade and gain knowledge in these areas. But it is a slow process. To speed things up, I founded Korvane platform which speeds up vetting process. Moreover, all the tests done in the process of strategy design is remembered by the platform. If there a study that can deliver reward expectations for the acceptable risk amount, it can be locked to produce the trading opportunities on any interval. This makes it easy to use model for busy people.

The rest of the book is not to make you experts in all trading areas but it is targeted to help busy people with enough understanding to help you learn, trade carefully knowing that options trading has different risk characteristics. You can refer to them in detail on PWT website. All studies published in this book does not guarantee a future success but they have produced results in the past. These should be taken as educational reference.
Updates

This design is for Print book. Below is about the author. Book needs to have bar code printed and ISBN listed on the back as well. Tomas Brennick, Founder, Korvane Markets Tomas is a computer science engineer with more than two decades of experience working for major financial institutions Vuma, RT Holdings, and PLWN. During his time at Orlundt Advisory Services, he spearheaded a large global delivery team, led business growth in Latin America from the ground up, and was directly responsible for customer experience and software delivery. During this time, he discovered the passion for trading options. Leveraging this against his extensive experience in computer software architecture, Tomas ventured out on his own to found and created www.korvanemarkets.example

Target Market(s)

Busy people with money and want to invest in stock market

Industry/Entity Type

Investment

Font styles to use
Sans Serif

Colors

Designer to choose colors to be used in the design.

Requirements
Must have
• 6 x 9 book. Title of book is "Steady Yield Contract Playbooks" and the subtitle is "for busy people". The author is Tomas Brennick.
• This is soft cover with 155 pages

```html
<!DOCTYPE html>
<html lang="en">
<head>
<meta charset="utf-8">
<title>Steady Yield Contract Playbooks — Cover</title>
<link rel="stylesheet" href="https://fonts.googleapis.com/css2?family=Montserrat:ital,wght@0,400;0,600;0,800;0,900;1,900&display=swap">
<style>
  :root {
    --cover-green: #2fa07a;
    --cover-green-dark: #278b69;
    --ink-navy: #2b2d6b;
    --brand-blue: #2c4fa3;
    --paper: #ffffff;
  }
  * { margin: 0; padding: 0; box-sizing: border-box; }
  html, body {
    width: 800px;
    height: 1200px;
    overflow: hidden;
    background: var(--paper);
  }
  .cover {
    position: relative;
    width: 800px;
    height: 1200px;
    overflow: hidden;
    font-family: "Montserrat", Arial, sans-serif;
  }
  .publisher-band {
    position: absolute;
    inset: 0 0 auto 0;
    height: 170px;
    background: var(--paper);
    display: flex;
    flex-direction: column;
    align-items: center;
    justify-content: center;
    gap: 6px;
  }
  .publisher-mark {
    display: flex;
    align-items: center;
    gap: 14px;
  }
  .publisher-square {
    width: 58px;
    height: 58px;
    background: var(--brand-blue);
    border-radius: 6px;
  }
  .publisher-name {
    font-size: 58px;
    font-weight: 800;
    color: var(--ink-navy);
    letter-spacing: -1px;
    line-height: 1;
  }
  .publisher-presents {
    font-size: 22px;
    font-weight: 600;
    color: var(--ink-navy);
    letter-spacing: 2px;
    margin-left: 120px;
  }
  .cover-field {
    position: absolute;
    top: 170px;
    left: 0;
    width: 800px;
    height: 1030px;
    background: radial-gradient(circle at 50% 40%, var(--cover-green) 0%, var(--cover-green-dark) 100%);
  }
  .title-block {
    position: absolute;
    top: 370px;
    left: 80px;
    transform: rotate(-8deg);
    transform-origin: left top;
  }
  .book-title {
    font-weight: 900;
    font-style: italic;
    font-size: 80px;
    line-height: 96px;
    text-transform: uppercase;
    letter-spacing: 0;
    white-space: nowrap;
  }
  .book-title span { display: block; }
  .title-light {
    color: var(--paper);
    text-shadow: 4px 4px 0 var(--ink-navy);
  }
  .title-dark {
    color: var(--ink-navy);
    text-shadow: 4px 4px 0 var(--paper);
  }
  .subtitle-banner {
    position: absolute;
    top: 770px;
    left: 385px;
    width: 345px;
    height: 54px;
    background: var(--ink-navy);
    transform: rotate(-8deg) skewX(-12deg);
    display: flex;
    align-items: center;
    justify-content: center;
  }
  .subtitle-text {
    transform: skewX(12deg);
    color: var(--paper);
    font-weight: 800;
    font-size: 29px;
    letter-spacing: 1px;
    text-transform: uppercase;
    white-space: nowrap;
  }
  .author-name {
    position: absolute;
    top: 1080px;
    left: 0;
    width: 800px;
    text-align: center;
    color: var(--paper);
    font-size: 32px;
    letter-spacing: 1px;
    text-transform: uppercase;
  }
  .author-first { font-weight: 600; }
  .author-last { font-weight: 800; }
</style>
</head>
<body>
  <main class="cover">
    <header class="publisher-band">
      <div class="publisher-mark">
        <div class="publisher-square"></div>
        <span class="publisher-name">Korvane</span>
      </div>
      <span class="publisher-presents">PRESENTS</span>
    </header>

    <div class="cover-field" role="img" aria-label="Green background with a faint pattern of finance and trading icons such as charts, coins and calculators"></div>

    <h1 class="title-block book-title">
      <span class="title-light">Steady</span>
      <span class="title-dark">Yield</span>
      <span class="title-light">Contract</span>
      <span class="title-dark">Playbooks</span>
    </h1>

    <div class="subtitle-banner">
      <span class="subtitle-text">For Busy People</span>
    </div>

    <p class="author-name"><span class="author-first">Tomas</span> <span class="author-last">Brennick</span></p>
  </main>
</body>
</html>
```